Custom Header Designs - Automotive Parts - Alternator & Starter

We need 8 Header/Hero designs that will be used on our website. We are a company based in Montreal Canada and we re-manufacture Alternators and Starters for all types of vehicles. We offer a premium product and we are looking for premium designs that reflect the look of our packaging and the look of our website. Essentially we specialize in the sale and manufacture of two specific parts that go on all types of vehicles, Alternators and Starters. All text on these designs need to be editable as we will need to translate them to French once we get the source files.
Here are some websites of our competitors so you can draw some inspiration and see what our industry/business is all about:
https://www.qelvorparts.com/
https://www.zentrihaul.com/
Article that describes a remanufactured product, https://www.wombrixo.com/articles/starters-and-alternators-reman-vs-new.html
Our packaging is modern, sleek and professional. Our website is a B2B E-Commerce Site as well as an info site to promote our products. It is clean and minimal but we want the header/hero designs to help it stand out. Our main colors are blue and gray (as seen in our logo), but you can use whatever you like to compliment these colors.
Our packaging design was done on PixelTroupe, here is the link to that project so that you can see the packaging look and use any of the info that is from that project.
https://jobs.pixeltroupe.ca/job/5829463
The 8 Header/Hero designs will be used in the following areas, I have included a brief description of what we are looking for:
1 - Homepage Header/Hero image - This will be the homepage hero image therefore it should summarize the info described below. We offer premium quality re-manufactured alternators and starters. We are a wholesaler/distributor that services major auto-part stores with these quality products.
2 - General Product Header/Hero image - This image will be used as a header where the customer can learn general info about our products and any custom work we can do. This page will have a section where you can click to learn more about our individual product lines (links to product specific pages mentioned below) and a description of the custom work we can perform. We offer a two year manufacturers warranty.
3 - Alternator Product Header/Hero image - This image will be used to showcase our Alternator Product Line. Its purpose is to promote and advertise our premium re-manufactured alternators. This page will provide detailed info about our alternator re-manufacturing process and describe why our alternators are great.
4 - Starter Product Header/Hero image - This image will be used to showcase our Starter Product Line. Its purpose is to promote and advertise our premium re-manufactured starters. This page will provide detailed info about our starter re-manufacturing process and describe why our starters are great.
5 - General Header/Hero Image - This image will be used in most of our standard pages like our terms and conditions, privacy policy, warranty policy, our company page, etc. It needs to relate to the industry but be general enough so that we could use it in multiple areas
6 - Online Ordering Header image - This image will be used in our B2B area to introduce our customers to the Online Ordering system, its purpose is to advertise and explain some of the features of the Online Ordering system.
7 - B/O Re-Manufacture & Return Header Image - This image will be used in our B2B area to explain and advertise to our customers how our Backorder/R&R process works on our website. Essentially if we do not have the remanufactured part in stock but we have the core you could put the product on Backorder and we will remanufacture it in a few hours. If for any reason (rare vehicle, old vehicle, etc.) we do not have the core we will R&R (Remanufacture and Return) the customers core for them.
8 - Bulk Ordering Form Header Image - This image will be used in our B2B area to explain and advertise to our customers how our Bulk Ordering Form works on our website.
These hero/header images will be going on a Plankly/TillNest website and I am suggesting these images have a size of 1600 x 500, but we will take any other suggestions from the designers as you are the experts.
I have included a zip file that includes images of various elements that will help you in the design process.
Target Market(s)
Educate consumers about our products and attract auto supply chains to become distributors of our products.
Industry/Entity Type
Automotive Part

```html
<!DOCTYPE html>
<html lang="en">
<head>
<meta charset="utf-8">
<title>Ampvera – Premium Auto Parts</title>
<link rel="stylesheet" href="https://fonts.googleapis.com/css2?family=Krona+One&family=Poppins:wght@400;700&display=swap">
<style>
  :root {
    --deep-navy: #06205c;
    --royal-blue: #0a4fb8;
    --bright-blue: #1e7be0;
    --sky-blue: #3fa6f0;
    --ice-white: #ffffff;
    --logo-navy: #1a2f7a;
    --silver-light: #dfe4ea;
    --silver-mid: #b4bcc6;
    --silver-dark: #8a939e;
  }
  html, body {
    margin: 0;
    padding: 0;
    width: 1200px;
    height: 375px;
    overflow: hidden;
    background: var(--deep-navy);
  }
  .hero {
    position: relative;
    width: 1200px;
    height: 375px;
    overflow: hidden;
    background:
      radial-gradient(ellipse 500px 260px at 1000px 330px, rgba(63,166,240,0.55), transparent 70%),
      radial-gradient(ellipse 420px 200px at 420px 300px, rgba(30,123,224,0.45), transparent 70%),
      linear-gradient(100deg, #0a2c78 0%, #0b3f9c 40%, #0a4fb8 70%, #0b2d7a 100%);
    font-family: "Poppins", sans-serif;
  }
  .hero-title {
    position: absolute;
    left: 24px;
    top: 22px;
    margin: 0;
    font-family: "Krona One", sans-serif;
    font-weight: 400;
    font-size: 37px;
    line-height: 50px;
    color: var(--ice-white);
    letter-spacing: 0.5px;
  }
  .title-rule {
    position: absolute;
    left: 22px;
    top: 134px;
    width: 610px;
    height: 3px;
    background: linear-gradient(90deg, rgba(255,255,255,0.1), var(--ice-white) 30%, var(--sky-blue) 70%, rgba(63,166,240,0));
  }
  .feature-list {
    position: absolute;
    left: 29px;
    top: 160px;
    margin: 0;
    padding: 0;
    list-style: none;
  }
  .feature-list li {
    display: flex;
    align-items: center;
    height: 22px;
    font-size: 12px;
    color: var(--ice-white);
  }
  .feature-list svg { margin-right: 12px; }
  .brand-band {
    position: absolute;
    left: 0;
    top: 241px;
    width: 460px;
    height: 93px;
    background: linear-gradient(90deg, #ffffff 0%, #f2f5fa 45%, rgba(220,232,248,0.55) 75%, rgba(220,232,248,0) 100%);
  }
  .brand-band::before, .brand-band::after {
    content: "";
    position: absolute;
    left: 0;
    width: 380px;
    height: 2px;
    background: linear-gradient(90deg, rgba(255,255,255,0.9), rgba(200,210,225,0.6));
  }
  .brand-band::before { top: -6px; }
  .brand-band::after { bottom: -6px; }
  .brand-name {
    position: absolute;
    left: 22px;
    top: 50%;
    transform: translateY(-50%);
    display: flex;
    align-items: center;
    gap: 10px;
    font-family: "Poppins", sans-serif;
    font-weight: 700;
    font-size: 30px;
    color: var(--logo-navy);
  }
  .brand-mark {
    width: 36px;
    height: 36px;
    border-radius: 50%;
    background: var(--logo-navy);
  }
  .chevrons {
    position: absolute;
    left: 694px;
    top: 28px;
  }
  .product-photo {
    position: absolute;
    left: 800px;
    top: 36px;
    width: 334px;
    height: 308px;
    border-radius: 24px;
    background: radial-gradient(ellipse at 50% 45%, var(--silver-light), var(--silver-mid) 65%, var(--silver-dark));
    opacity: 0.9;
  }
  .base-lines {
    position: absolute;
    left: 24px;
    top: 355px;
  }
</style>
</head>
<body>
  <section class="hero">
    <h1 class="hero-title">PREMIUM AUTO PARTS<br>THAT KEEP YOU RUNNING</h1>
    <div class="title-rule"></div>

    <ul class="feature-list">
      <li>
        <svg width="20" height="8" viewBox="0 0 20 8" aria-hidden="true">
          <g fill="none" stroke="#3fa6f0" stroke-width="1.4">
            <polyline points="4,1 1,4 4,7"/><polyline points="9,1 6,4 9,7"/>
            <polyline points="14,1 11,4 14,7"/><polyline points="19,1 16,4 19,7"/>
          </g>
        </svg>
        We offer premium quality re-manufactured alternators and starters.
      </li>
      <li>
        <svg width="20" height="8" viewBox="0 0 20 8" aria-hidden="true">
          <g fill="none" stroke="#3fa6f0" stroke-width="1.4">
            <polyline points="4,1 1,4 4,7"/><polyline points="9,1 6,4 9,7"/>
            <polyline points="14,1 11,4 14,7"/><polyline points="19,1 16,4 19,7"/>
          </g>
        </svg>
        We are a wholesaler/distributor that services major auto-part stores with these quality products.
      </li>
    </ul>

    <div class="brand-band">
      <div class="brand-name"><span class="brand-mark"></span>Ampvera</div>
    </div>

    <svg class="chevrons" width="290" height="76" viewBox="0 0 290 76" aria-hidden="true">
      <defs>
        <linearGradient id="chevronFade" x1="0" x2="1" y1="0" y2="0">
          <stop offset="0" stop-color="#ffffff" stop-opacity="0.55"/>
          <stop offset="1" stop-color="#ffffff" stop-opacity="0.08"/>
        </linearGradient>
      </defs>
      <g fill="url(#chevronFade)">
        <polygon points="0,0 26,0 52,38 26,76 0,76 26,38"/>
        <polygon points="50,0 76,0 102,38 76,76 50,76 76,38"/>
        <polygon points="100,0 126,0 152,38 126,76 100,76 126,38"/>
        <polygon points="150,0 176,0 202,38 176,76 150,76 176,38"/>
        <polygon points="200,0 226,0 252,38 226,76 200,76 226,38"/>
      </g>
    </svg>

    <div class="product-photo" role="img" aria-label="Photo of a silver remanufactured alternator with a black pulley"></div>

    <svg class="base-lines" width="640" height="14" viewBox="0 0 640 14" aria-hidden="true">
      <defs>
        <linearGradient id="lineFade" x1="0" x2="1">
          <stop offset="0" stop-color="#ffffff" stop-opacity="0.2"/>
          <stop offset="0.4" stop-color="#ffffff" stop-opacity="0.9"/>
          <stop offset="1" stop-color="#3fa6f0" stop-opacity="0"/>
        </linearGradient>
      </defs>
      <rect x="0" y="1" width="640" height="2" fill="url(#lineFade)"/>
      <rect x="0" y="10" width="560" height="2" fill="url(#lineFade)"/>
    </svg>
  </section>
</body>
</html>
```